Quiz Board Game

We would like a graphic design for our physical game board. The image shows the hand made prototype. We will stress that the prototype should not be regarded as anything else than a prototype. This means that all the colors and graphics on the prototype are subject to change in the production version. That said, the start shape and fields around the endges should remain as is. It should fit on a board with dimension: 600mm x 600mm. Please disregard the puzzle-pattern. This is for the prototype production only. The production board will be 4-folded.

There are 6 different colors on the board. These represents categories in the game. We would like the designer to find the best colors for this purpose. The colors should be easily distinguishable, and also provide a nice color scheme for the eyes. At the same time we will need to produce pawns and gems with the same colors, so it is probably wise not to be too creative. Suggestions are some shade of: red, blue, yellow, orange, green, purple.

There are 6 main/large fields, one for each color. These are special award fields, and should stand out and have a nice symbol in it, ie: a gem.

There are 36 ordinary fields, 6 for each color. The placement of the different fields/colors should stay as in the prototype, but of course the colors themselfs should be different, as stated before. 6 of these fields have a question marks in them. Please find a nice way to represent this.

There are 6 fields with a dice. These should have a gray background and the provided symbol with the new colors as sectors.

There are 6 outlined areas on the board, one in each sector. Cards with category names will be places on these areas. The shaping and placement of these areas could be different from the prototype. It should for instance probably be a little higher.

In each color triangle there are 6 round (white) placeholders. These will be used to place physical gems. The background should be neutral, white or light gray, so it will not interfer with the translucent gem colors.

In the center of the board we would like to keep the dice symbol, but it should be designed as a new dice.

The blank area around the board should be filled with a neutral color and maybe som graphic. Here there should also be room for the games name (which is not decided yet).

We will also need graphic design of the box. The design should be simple and elegant, with not many colors.

```html
<!DOCTYPE html>
<html lang="en">
<head>
<meta charset="utf-8">
<title>Quiz Board Game – Board Layout</title>
<link href="https://fonts.googleapis.com/css2?family=Arimo:wght@700&display=swap" rel="stylesheet">
<style>
  :root {
    --red: #e8453c;
    --purple: #a93c91;
    --orange: #e98c38;
    --blue: #22649c;
    --yellow: #f4d35e;
    --green: #66b38c;
    --ink: #231f20;
    --field-dark: #333233;
    --paper: #ffffff;
  }
  html, body {
    margin: 0;
    padding: 0;
    width: 1200px;
    height: 1200px;
    overflow: hidden;
    background: var(--paper);
  }
  .artboard { display: block; width: 1200px; height: 1200px; }
  .dimension-line { stroke: var(--ink); stroke-width: 1.5; fill: none; }
  .dimension-label {
    font-family: "Arimo", Arial, sans-serif;
    font-weight: 700;
    font-size: 22px;
    fill: #000;
  }
  .board-outline { fill: url(#darkField); stroke: var(--ink); stroke-width: 8; stroke-linejoin: round; }
  .arm--red { --c: var(--red); }
  .arm--purple { --c: var(--purple); }
  .arm--orange { --c: var(--orange); }
  .arm--blue { --c: var(--blue); }
  .arm--yellow { --c: var(--yellow); }
  .arm--green { --c: var(--green); }
  .sector { fill: var(--c); }
  .sector-shade { fill: url(#sectorShade); }
  .home { fill: var(--c); stroke: var(--ink); stroke-width: 3; }
  .gem-holder { fill: #fff; opacity: 0.85; }
  .award-field { fill: var(--c); stroke: var(--ink); stroke-width: 6; stroke-linejoin: round; }
  .award-gem { fill: url(#gemGlow); stroke: rgba(255,255,255,0.7); stroke-width: 2; }
  .card-area { fill: var(--c); stroke: var(--ink); stroke-width: 2; }
  .card-shade { fill: rgba(0,0,0,0.08); }
  .cell { stroke: var(--ink); stroke-width: 6; stroke-linejoin: round; }
  .cell--red { fill: var(--red); }
  .cell--purple { fill: var(--purple); }
  .cell--orange { fill: var(--orange); }
  .cell--blue { fill: var(--blue); }
  .cell--yellow { fill: var(--yellow); }
  .cell--green { fill: var(--green); }
  .question-mark {
    font-family: "Arimo", Arial, sans-serif;
    font-weight: 700;
    font-size: 78px;
    fill: #fff;
    stroke: var(--ink);
    stroke-width: 6;
    paint-order: stroke;
    text-anchor: middle;
    dominant-baseline: central;
  }
  .dice-glow { fill: url(#diceGlow); }
  .hex-line { stroke: var(--ink); stroke-width: 2; }
  .centre-die { fill: #fff; stroke: var(--ink); stroke-width: 6; stroke-linejoin: round; }
  .dice-face { fill: #fff; stroke: var(--ink); stroke-width: 2; }
</style>
</head>
<body>
<svg class="artboard" viewBox="0 0 1920 1920" xmlns="http://www.w3.org/2000/svg">
  <defs>
    <radialGradient id="darkField" cx="50%" cy="50%" r="50%">
      <stop offset="0" stop-color="#4a4949"/>
      <stop offset="1" stop-color="#262425"/>
    </radialGradient>
    <linearGradient id="sectorShade" gradientUnits="userSpaceOnUse" x1="0" y1="-388" x2="0" y2="0">
      <stop offset="0" stop-color="#000" stop-opacity="0.3"/>
      <stop offset="1" stop-color="#000" stop-opacity="0"/>
    </linearGradient>
    <radialGradient id="gemGlow" cx="50%" cy="50%" r="50%">
      <stop offset="0" stop-color="#fff" stop-opacity="0.35"/>
      <stop offset="1" stop-color="#fff" stop-opacity="0.85"/>
    </radialGradient>
    <radialGradient id="diceGlow" cx="50%" cy="50%" r="50%">
      <stop offset="0" stop-color="#9a9a9a"/>
      <stop offset="1" stop-color="#2b2a2a" stop-opacity="0"/>
    </radialGradient>
  </defs>

  <!-- Dimension markers -->
  <g class="dimensions">
    <polyline class="dimension-line" points="282,60 282,89 1650,89 1650,119"/>
    <text class="dimension-label" x="300" y="78">500 mm</text>
    <polyline class="dimension-line" points="142,167 172,167 172,1782 201,1782"/>
    <text class="dimension-label" transform="translate(148,286) rotate(-90)">590 mm</text>
  </g>

  <g class="board" transform="translate(965,975)">
    <polygon class="board-outline" points="0,-804 294,-510 696,-402 589,0 696,402 294,510 0,804 -294,510 -696,402 -589,0 -696,-402 -294,-510"/>

    <!-- Arm template repeated six times -->
    <g class="arm arm--red" transform="rotate(0)">
      <polygon class="sector" points="-224,-388 224,-388 0,0"/>
      <polygon class="sector-shade" points="-224,-388 224,-388 0,0"/>
      <polygon class="card-area" points="-120,-388 120,-388 114,-345 -114,-345"/>
      <polygon class="home" points="-224,-388 224,-388 0,-612"/>
      <g class="gem-holders">
        <circle class="gem-holder" cx="0" cy="-565" r="24"/>
        <circle class="gem-holder" cx="-46" cy="-500" r="24"/>
        <circle class="gem-holder" cx="46" cy="-500" r="24"/>
        <circle class="gem-holder" cx="-103" cy="-440" r="24"/>
        <circle class="gem-holder" cx="0" cy="-440" r="24"/>
        <circle class="gem-holder" cx="103" cy="-440" r="24"/>
      </g>
      <polygon class="cell cell--yellow" points="-165,-447 -261,-543 -206,-598 -110,-502"/>
      <polygon class="cell cell--green" points="-110,-502 -206,-598 -151,-653 -55,-557"/>
      <polygon class="cell cell--purple" points="-55,-557 -151,-653 -96,-708 0,-612"/>
      <polygon class="cell cell--orange" points="55,-557 151,-653 96,-708 0,-612"/>
      <polygon class="cell cell--blue" points="110,-502 206,-598 151,-653 55,-557"/>
      <polygon class="cell cell--red" points="165,-447 261,-543 206,-598 110,-502"/>
      <text class="question-mark" transform="translate(75,-632) rotate(-45)">¿</text>
      <polygon class="award-field" points="0,-612 -96,-708 0,-804 96,-708"/>
      <circle class="award-gem" cx="0" cy="-708" r="50" role="img" aria-label="Red award gem symbol"/>
      <circle class="dice-glow" cx="261" cy="-452" r="62"/>
      <g role="img" aria-label="Dice field symbol with six category colour sectors" transform="translate(261,-452)">
        <polygon points="0,0 0,-38 33,-19" fill="var(--red)"/>
        <polygon points="0,0 33,-19 33,19" fill="var(--purple)"/>
        <polygon points="0,0 33,19 0,38" fill="var(--orange)"/>
        <polygon points="0,0 0,38 -33,19" fill="var(--blue)"/>
        <polygon points="0,0 -33,19 -33,-19" fill="var(--yellow)"/>
        <polygon points="0,0 -33,-19 0,-38" fill="var(--green)"/>
        <rect class="dice-face" x="-17" y="-17" width="34" height="34" rx="6"/>
      </g>
    </g>

    <g class="arm arm--purple" transform="rotate(60)">
      <polygon class="sector" points="-224,-388 224,-388 0,0"/>
      <polygon class="sector-shade" points="-224,-388 224,-388 0,0"/>
      <polygon class="card-area" points="-120,-388 120,-388 114,-345 -114,-345"/>
      <polygon class="home" points="-224,-388 224,-388 0,-612"/>
      <g class="gem-holders">
        <circle class="gem-holder" cx="0" cy="-565" r="24"/>
        <circle class="gem-holder" cx="-46" cy="-500" r="24"/>
        <circle class="gem-holder" cx="46" cy="-500" r="24"/>
        <circle class="gem-holder" cx="-103" cy="-440" r="24"/>
        <circle class="gem-holder" cx="0" cy="-440" r="24"/>
        <circle class="gem-holder" cx="103" cy="-440" r="24"/>
      </g>
      <polygon class="cell cell--purple" points="-165,-447 -261,-543 -206,-598 -110,-502"/>
      <polygon class="cell cell--orange" points="-110,-502 -206,-598 -151,-653 -55,-557"/>
      <polygon class="cell cell--blue" points="-55,-557 -151,-653 -96,-708 0,-612"/>
      <polygon class="cell cell--red" points="55,-557 151,-653 96,-708 0,-612"/>
      <polygon class="cell cell--green" points="110,-502 206,-598 151,-653 55,-557"/>
      <polygon class="cell cell--yellow" points="165,-447 261,-543 206,-598 110,-502"/>
      <text class="question-mark" transform="translate(130,-577) rotate(-135)">?</text>
      <polygon class="award-field" points="0,-612 -96,-708 0,-804 96,-708"/>
      <circle class="award-gem" cx="0" cy="-708" r="50" role="img" aria-label="Purple award gem symbol"/>
      <circle class="dice-glow" cx="261" cy="-452" r="62"/>
      <g role="img" aria-label="Dice field symbol with six category colour sectors" transform="translate(261,-452) rotate(-60)">
        <polygon points="0,0 0,-38 33,-19" fill="var(--red)"/>
        <polygon points="0,0 33,-19 33,19" fill="var(--purple)"/>
        <polygon points="0,0 33,19 0,38" fill="var(--orange)"/>
        <polygon points="0,0 0,38 -33,19" fill="var(--blue)"/>
        <polygon points="0,0 -33,19 -33,-19" fill="var(--yellow)"/>
        <polygon points="0,0 -33,-19 0,-38" fill="var(--green)"/>
        <rect class="dice-face" x="-17" y="-17" width="34" height="34" rx="6"/>
      </g>
    </g>

    <g class="arm arm--orange" transform="rotate(120)">
      <polygon class="sector" points="-224,-388 224,-388 0,0"/>
      <polygon class="sector-shade" points="-224,-388 224,-388 0,0"/>
      <polygon class="card-area" points="-120,-388 120,-388 114,-345 -114,-345"/>
      <polygon class="home" points="-224,-388 224,-388 0,-612"/>
      <g class="gem-holders">
        <circle class="gem-holder" cx="0" cy="-565" r="24"/>
        <circle class="gem-holder" cx="-46" cy="-500" r="24"/>
        <circle class="gem-holder" cx="46" cy="-500" r="24"/>
        <circle class="gem-holder" cx="-103" cy="-440" r="24"/>
        <circle class="gem-holder" cx="0" cy="-440" r="24"/>
        <circle class="gem-holder" cx="103" cy="-440" r="24"/>
      </g>
      <polygon class="cell cell--orange" points="-165,-447 -261,-543 -206,-598 -110,-502"/>
      <polygon class="cell cell--purple" points="-110,-502 -206,-598 -151,-653 -55,-557"/>
      <polygon class="cell cell--red" points="-55,-557 -151,-653 -96,-708 0,-612"/>
      <polygon class="cell cell--green" points="55,-557 151,-653 96,-708 0,-612"/>
      <polygon class="cell cell--blue" points="110,-502 206,-598 151,-653 55,-557"/>
      <polygon class="cell cell--yellow" points="165,-447 261,-543 206,-598 110,-502"/>
      <text class="question-mark" transform="translate(185,-522) rotate(-120)">?</text>
      <polygon class="award-field" points="0,-612 -96,-708 0,-804 96,-708"/>
      <circle class="award-gem" cx="0" cy="-708" r="50" role="img" aria-label="Orange award gem symbol"/>
      <circle class="dice-glow" cx="261" cy="-452" r="62"/>
      <g role="img" aria-label="Dice field symbol with six category colour sectors" transform="translate(261,-452) rotate(-120)">
        <polygon points="0,0 0,-38 33,-19" fill="var(--red)"/>
        <polygon points="0,0 33,-19 33,19" fill="var(--purple)"/>
        <polygon points="0,0 33,19 0,38" fill="var(--orange)"/>
        <polygon points="0,0 0,38 -33,19" fill="var(--blue)"/>
        <polygon points="0,0 -33,19 -33,-19" fill="var(--yellow)"/>
        <polygon points="0,0 -33,-19 0,-38" fill="var(--green)"/>
        <rect class="dice-face" x="-17" y="-17" width="34" height="34" rx="6"/>
      </g>
    </g>

    <g class="arm arm--blue" transform="rotate(180)">
      <polygon class="sector" points="-224,-388 224,-388 0,0"/>
      <polygon class="sector-shade" points="-224,-388 224,-388 0,0"/>
      <polygon class="card-area" points="-120,-388 120,-388 114,-345 -114,-345"/>
      <polygon class="home" points="-224,-388 224,-388 0,-612"/>
      <g class="gem-holders">
        <circle class="gem-holder" cx="0" cy="-565" r="24"/>
        <circle class="gem-holder" cx="-46" cy="-500" r="24"/>
        <circle class="gem-holder" cx="46" cy="-500" r="24"/>
        <circle class="gem-holder" cx="-103" cy="-440" r="24"/>
        <circle class="gem-holder" cx="0" cy="-440" r="24"/>
        <circle class="gem-holder" cx="103" cy="-440" r="24"/>
      </g>
      <polygon class="cell cell--purple" points="-165,-447 -261,-543 -206,-598 -110,-502"/>
      <polygon class="cell cell--green" points="-110,-502 -206,-598 -151,-653 -55,-557"/>
      <polygon class="cell cell--orange" points="-55,-557 -151,-653 -96,-708 0,-612"/>
      <polygon class="cell cell--yellow" points="55,-557 151,-653 96,-708 0,-612"/>
      <polygon class="cell cell--red" points="110,-502 206,-598 151,-653 55,-557"/>
      <polygon class="cell cell--blue" points="165,-447 261,-543 206,-598 110,-502"/>
      <text class="question-mark" transform="translate(130,-577) rotate(-225)">?</text>
      <polygon class="award-field" points="0,-612 -96,-708 0,-804 96,-708"/>
      <circle class="award-gem" cx="0" cy="-708" r="50" role="img" aria-label="Blue award gem symbol"/>
      <circle class="dice-glow" cx="261" cy="-452" r="62"/>
      <g role="img" aria-label="Dice field symbol with six category colour sectors" transform="translate(261,-452) rotate(-180)">
        <polygon points="0,0 0,-38 33,-19" fill="var(--red)"/>
        <polygon points="0,0 33,-19 33,19" fill="var(--purple)"/>
        <polygon points="0,0 33,19 0,38" fill="var(--orange)"/>
        <polygon points="0,0 0,38 -33,19" fill="var(--blue)"/>
        <polygon points="0,0 -33,19 -33,-19" fill="var(--yellow)"/>
        <polygon points="0,0 -33,-19 0,-38" fill="var(--green)"/>
        <rect class="dice-face" x="-17" y="-17" width="34" height="34" rx="6"/>
      </g>
    </g>

    <g class="arm arm--yellow" transform="rotate(240)">
      <polygon class="sector" points="-224,-388 224,-388 0,0"/>
      <polygon class="sector-shade" points="-224,-388 224,-388 0,0"/>
      <polygon class="card-area" points="-120,-388 120,-388 114,-345 -114,-345"/>
      <polygon class="home" points="-224,-388 224,-388 0,-612"/>
      <g class="gem-holders">
        <circle class="gem-holder" cx="0" cy="-565" r="24"/>
        <circle class="gem-holder" cx="-46" cy="-500" r="24"/>
        <circle class="gem-holder" cx="46" cy="-500" r="24"/>
        <circle class="gem-holder" cx="-103" cy="-440" r="24"/>
        <circle class="gem-holder" cx="0" cy="-440" r="24"/>
        <circle class="gem-holder" cx="103" cy="-440" r="24"/>
      </g>
      <polygon class="cell cell--orange" points="-165,-447 -261,-543 -206,-598 -110,-502"/>
      <polygon class="cell cell--yellow" points="-110,-502 -206,-598 -151,-653 -55,-557"/>
      <polygon class="cell cell--green" points="-55,-557 -151,-653 -96,-708 0,-612"/>
      <polygon class="cell cell--purple" points="55,-557 151,-653 96,-708 0,-612"/>
      <polygon class="cell cell--blue" points="110,-502 206,-598 151,-653 55,-557"/>
      <polygon class="cell cell--red" points="165,-447 261,-543 206,-598 110,-502"/>
      <text class="question-mark" transform="translate(130,-577) rotate(-285)">¿</text>
      <polygon class="award-field" points="0,-612 -96,-708 0,-804 96,-708"/>
      <circle class="award-gem" cx="0" cy="-708" r="50" role="img" aria-label="Yellow award gem symbol"/>
      <circle class="dice-glow" cx="261" cy="-452" r="62"/>
      <g role="img" aria-label="Dice field symbol with six category colour sectors" transform="translate(261,-452) rotate(-240)">
        <polygon points="0,0 0,-38 33,-19" fill="var(--red)"/>
        <polygon points="0,0 33,-19 33,19" fill="var(--purple)"/>
        <polygon points="0,0 33,19 0,38" fill="var(--orange)"/>
        <polygon points="0,0 0,38 -33,19" fill="var(--blue)"/>
        <polygon points="0,0 -33,19 -33,-19" fill="var(--yellow)"/>
        <polygon points="0,0 -33,-19 0,-38" fill="var(--green)"/>
        <rect class="dice-face" x="-17" y="-17" width="34" height="34" rx="6"/>
      </g>
    </g>

    <g class="arm arm--green" transform="rotate(300)">
      <polygon class="sector" points="-224,-388 224,-388 0,0"/>
      <polygon class="sector-shade" points="-224,-388 224,-388 0,0"/>
      <polygon class="card-area" points="-120,-388 120,-388 114,-345 -114,-345"/>
      <polygon class="home" points="-224,-388 224,-388 0,-612"/>
      <g class="gem-holders">
        <circle class="gem-holder" cx="0" cy="-565" r="24"/>
        <circle class="gem-holder" cx="-46" cy="-500" r="24"/>
        <circle class="gem-holder" cx="46" cy="-500" r="24"/>
        <circle class="gem-holder" cx="-103" cy="-440" r="24"/>
        <circle class="gem-holder" cx="0" cy="-440" r="24"/>
        <circle class="gem-holder" cx="103" cy="-440" r="24"/>
      </g>
      <polygon class="cell cell--green" points="-165,-447 -261,-543 -206,-598 -110,-502"/>
      <polygon class="cell cell--orange" points="-110,-502 -206,-598 -151,-653 -55,-557"/>
      <polygon class="cell cell--yellow" points="-55,-557 -151,-653 -96,-708 0,-612"/>
      <polygon class="cell cell--purple" points="55,-557 151,-653 96,-708 0,-612"/>
      <polygon class="cell cell--red" points="110,-502 206,-598 151,-653 55,-557"/>
      <polygon class="cell cell--blue" points="165,-447 261,-543 206,-598 110,-502"/>
      <text class="question-mark" transform="translate(75,-632) rotate(-285)">¿</text>
      <polygon class="award-field" points="0,-612 -96,-708 0,-804 96,-708"/>
      <circle class="award-gem" cx="0" cy="-708" r="50" role="img" aria-label="Green award gem symbol"/>
      <circle class="dice-glow" cx="261" cy="-452" r="62"/>
      <g role="img" aria-label="Dice field symbol with six category colour sectors" transform="translate(261,-452) rotate(-300)">
        <polygon points="0,0 0,-38 33,-19" fill="var(--red)"/>
        <polygon points="0,0 33,-19 33,19" fill="var(--purple)"/>
        <polygon points="0,0 33,19 0,38" fill="var(--orange)"/>
        <polygon points="0,0 0,38 -33,19" fill="var(--blue)"/>
        <polygon points="0,0 -33,19 -33,-19" fill="var(--yellow)"/>
        <polygon points="0,0 -33,-19 0,-38" fill="var(--green)"/>
        <rect class="dice-face" x="-17" y="-17" width="34" height="34" rx="6"/>
      </g>
    </g>

    <!-- Sector dividers -->
    <g class="hex-lines">
      <line class="hex-line" x1="-224" y1="-388" x2="224" y2="388"/>
      <line class="hex-line" x1="224" y1="-388" x2="-224" y2="388"/>
      <line class="hex-line" x1="-448" y1="0" x2="448" y2="0"/>
    </g>

    <!-- Central die -->
    <polygon class="centre-die" role="img" aria-label="Central die symbol" points="0,-92 80,-46 80,46 0,92 -80,46 -80,-46"/>
  </g>
</svg>
</body>
</html>
```